KRT Design Business Card

I need to develop a business card for my real estate design and investment company. Something clean, classic and professional with a modern vibe.

Industry/Entity Type

Real Estate

Font styles to use
Serif
Sans Serif

```html
<!DOCTYPE html>
<html lang="en">
<head>
<meta charset="utf-8">
<title>KRT Design Business Card</title>
<link href="https://fonts.googleapis.com/css2?family=Arimo:wght@400;700&display=swap" rel="stylesheet">
<style>
  :root {
    --backdrop: #e4e4e4;
    --paper: #fbfbfb;
    --ink: #111111;
    --card-black: #161616;
    --paper-white: #ffffff;
  }
  * { margin: 0; padding: 0; box-sizing: border-box; }
  html, body {
    width: 1200px; height: 720px; overflow: hidden;
    background: var(--backdrop);
    font-family: "Arimo", Arial, sans-serif;
  }
  .canvas { position: relative; width: 1200px; height: 720px; }
  .card {
    position: absolute; top: 242px;
    width: 420px; height: 240px; overflow: hidden;
  }
  .card-front { left: 147px; background: var(--paper); color: var(--ink); }
  .card-back { left: 633px; background: var(--card-black); color: var(--paper-white); }

  .name-tab {
    position: absolute; left: 0; top: 29px;
    width: 9px; height: 36px; background: var(--ink);
  }
  .holder { position: absolute; left: 18px; top: 35px; }
  .holder-name { font-size: 13px; font-weight: 400; line-height: 16px; }
  .holder-title { font-size: 9.5px; line-height: 12px; }

  .address {
    position: absolute; left: 18px; top: 104px; width: 150px;
    font-size: 9.5px; line-height: 12px;
  }
  .contacts {
    position: absolute; left: 18px; top: 143px; list-style: none;
    font-size: 9.5px; line-height: 12px;
  }
  .contacts li { display: flex; align-items: center; gap: 7px; }
  .contacts svg { width: 10px; height: 10px; fill: var(--ink); }

  .front-wordmark {
    position: absolute; right: 22px; top: 176px;
    font-size: 24px; font-weight: 400; letter-spacing: 1px;
  }
  .bottom-band {
    position: absolute; left: 0; bottom: 0;
    width: 100%; height: 18px; background: var(--ink);
  }

  .back-wordmark {
    position: absolute; left: 0; right: 0; top: 104px;
    text-align: center; font-size: 32px; font-weight: 400; letter-spacing: 1.5px;
  }
</style>
</head>
<body>
<main class="canvas">
  <section class="card card-front">
    <div class="name-tab"></div>
    <div class="holder">
      <p class="holder-name">Daniel Hart</p>
      <p class="holder-title">Founder &amp; CEO</p>
    </div>
    <p class="address">Here your compnay or home address</p>
    <ul class="contacts">
      <li>
        <svg viewBox="0 0 10 10" aria-hidden="true"><path d="M1 3.5C1 2 3 1.5 5 1.5S9 2 9 3.5L7.5 4 7 3H3L2.5 4ZM2.5 5h5L8.5 9h-7Z"/></svg>
        <span>+986 214 730</span>
      </li>
      <li>
        <svg viewBox="0 0 10 10" aria-hidden="true"><path d="M3 0.5h4v9H3Zm0.8 1v6h2.4v-6Z"/></svg>
        <span>+985 362 918</span>
      </li>
      <li>
        <svg viewBox="0 0 10 10" aria-hidden="true"><path d="M0.5 2h9v6h-9Zm1 1 3.5 2.6L8.5 3Z"/></svg>
        <span>info@krtdesign.com</span>
      </li>
      <li>
        <svg viewBox="0 0 10 10" aria-hidden="true"><path d="M0.5 1.5h9v6h-3.5v1h1.5v1h-5v-1h1.5v-1h-3.5Zm1 1v4h7v-4Z"/></svg>
        <span>www.krtdesign.com</span>
      </li>
    </ul>
    <p class="front-wordmark">KRT Design</p>
    <div class="bottom-band"></div>
  </section>

  <section class="card card-back">
    <p class="back-wordmark">KRT Design</p>
  </section>
</main>
</body>
</html>
```